Harlow Mechanical Contractors needs a Website

Create basic website for commercial plumbing and mechanical contractor; to include pictures of works in progress and completed works, description of all services offered and geographical locations and licenses

Target Market(s)

General Contractors, Real Estate Developers, Construction Companies

Industry/Entity Type

Construction

Coding

Coded - Design and coding required

Number of Pages Required

5+ page

Font styles to use

Colors
0392cd

```html
<!DOCTYPE html>
<html lang="en">
<head>
<meta charset="utf-8">
<title>Harlow Mechanical Contractors</title>
<link href="https://fonts.googleapis.com/css2?family=Roboto:wght@400;500;700&family=Raleway:wght@400;500;600&display=swap" rel="stylesheet">
<style>
:root{
  --navy:#1f4f7a;
  --brand:#22507f;
  --accent:#0392cd;
  --ink:#333;
  --muted:#555;
  --rule:#2c6a9a;
  --tile-a:#2b6a8f;
  --tile-b:#4a4a4a;
  --tile-c:#1e4a78;
  --tile-d:#7a7a7a;
  --band:#2d5f8e;
  --footer:#2b2b2b;
  --white:#fff;
}
*{box-sizing:border-box;margin:0;padding:0}
html,body{width:1200px;height:2740px;overflow:hidden;background:#fff}
body{font-family:"Raleway",sans-serif;color:var(--ink)}
.page{position:relative;width:1200px;height:2740px;overflow:hidden}
.abs{position:absolute}
.head{font-family:"Roboto",sans-serif}

/* top bar */
.topbar{left:0;top:0;width:1200px;height:44px;background:var(--navy)}
.topbar .phone{left:694px;top:11px;color:#fff;font:500 16px "Roboto",sans-serif;display:flex;align-items:center;gap:10px}
.topbar .divider{left:868px;top:10px;width:1px;height:24px;background:#fff;opacity:.7}
.topbar .social{left:905px;top:15px;display:flex;gap:34px}
.topbar .social span{width:13px;height:13px;border-radius:50%;background:#fff;opacity:.9}

/* header */
.header{left:0;top:44px;width:1200px;height:87px;background:#fff;box-shadow:0 1px 3px rgba(0,0,0,.12)}
.brand{left:100px;top:20px;display:flex;align-items:center;gap:10px;z-index:3}
.brand .mark{width:112px;height:112px;border-radius:50%;background:#fff;box-shadow:0 2px 6px rgba(0,0,0,.15)}
.brand .name{font:700 15px "Roboto",sans-serif;color:var(--brand);line-height:1.1;width:120px;text-transform:uppercase}
.nav{left:588px;top:97px;display:flex;font:400 16px "Roboto",sans-serif;color:var(--ink)}
.nav a{color:inherit;text-decoration:none;position:absolute;white-space:nowrap}
.nav .active{color:var(--brand);font-weight:500}
.nav .active::after{content:"";position:absolute;left:0;right:0;top:28px;height:3px;background:var(--brand)}

/* hero */
.hero{left:0;top:131px;width:1200px;height:504px;background:linear-gradient(120deg,#5b5550 0%,#8a8680 35%,#6d6a66 60%,#3f3d3b 100%)}
.hero-title{left:0;top:276px;width:1200px;text-align:center;font:500 40px "Roboto",sans-serif;color:#fff}
.hero-sub{left:0;top:350px;width:1200px;text-align:center;font:400 16px/29px "Raleway",sans-serif;color:#fff}
.hero-arrow{top:362px}

/* service circles */
.circle{width:248px;height:248px;border-radius:50%;border:10px solid #a9a9a9;top:524px}
.circle.mid{border-color:#6f93ad}
.svc-title{top:790px;width:300px;text-align:center;font:500 19px "Roboto",sans-serif;color:var(--brand);text-transform:uppercase}
.svc-text{top:820px;width:270px;text-align:center;font:400 12.5px/22px "Raleway",sans-serif;color:var(--ink)}
.svc-more{top:903px;width:300px;text-align:center;font:500 14px "Roboto",sans-serif;color:var(--brand);display:flex;justify-content:center;align-items:center;gap:10px}

.rule{height:2px;background:var(--rule)}

.sec-title{display:flex;align-items:center;gap:14px;font:700 29px "Roboto",sans-serif;color:var(--brand);text-transform:uppercase}
.sec-title .dot{width:34px;height:34px;border-radius:50%;background:var(--brand)}
.intro{left:150px;top:1070px;width:900px;text-align:center;font:400 12.5px/22px "Raleway",sans-serif;color:var(--ink)}

.tile{top:1194px;width:234px;height:196px;color:#fff;text-align:center}
.tile svg{position:absolute;left:77px;top:34px}
.tile .label{position:absolute;left:0;right:0;top:143px;font:500 19px "Roboto",sans-serif;text-transform:uppercase}

/* band */
.band{left:0;top:1437px;width:1200px;height:499px;background:linear-gradient(90deg,#2b5b8a 0%,#356893 50%,#2b5b8a 100%)}
.band-title{font:500 28px "Roboto",sans-serif;color:#fff;display:flex;align-items:center;gap:12px}
.band-title .dot{width:38px;height:38px;border-radius:50%;background:#fff}
.card{top:1569px;width:273px;height:312px;background:#fff;padding:6px}
.card .photo{width:261px;height:144px}
.card h3{margin:18px 0 0 0;font:500 16px "Roboto",sans-serif;color:#222}
.card p{margin-top:8px;font:400 12px/19px "Raleway",sans-serif;color:#444;width:250px}
.card .btn{position:absolute;left:12px;top:264px;width:108px;height:33px;color:#fff;font:400 13px/33px "Roboto",sans-serif;text-align:center}
.pop-thumb{left:716px;width:95px;height:84px;border:3px solid #fff}
.pop-title{left:831px;font:500 18px "Roboto",sans-serif;color:#fff}
.pop-text{left:831px;width:270px;font:400 12px/20px "Raleway",sans-serif;color:#e6eef5}
.pop-rule{left:831px;width:270px;height:1px;background:rgba(255,255,255,.45)}

/* why */
.feature-title{top:2078px;font:500 21px "Roboto",sans-serif;color:var(--brand)}
.feature-text{top:2112px;width:230px;font:400 12.5px/22px "Raleway",sans-serif;color:var(--muted)}
.feature-icon{top:2080px}

.partners{left:146px;top:2255px;width:914px;height:80px;display:flex;align-items:center;justify-content:space-between}
.partner{width:120px;display:flex;justify-content:center}
.partner-sep{width:1px;height:50px;background:#ccc}
.round-arrow{top:2275px;width:36px;height:36px;border:2px solid #333;border-radius:50%}

/* footer */
.footer{left:0;top:2380px;width:1200px;height:305px;background:linear-gradient(90deg,#262626,#333 50%,#2a2a2a)}
.f-brand{left:99px;top:2505px;display:flex;align-items:center;gap:10px}
.f-brand .mark{width:60px;height:60px;border-radius:50%;border:5px solid #fff}
.f-brand .name{font:700 16px/1.1 "Roboto",sans-serif;color:#fff;text-transform:uppercase;width:120px}
.f-head{top:2436px;font:500 19px "Roboto",sans-serif;color:#fff;text-transform:uppercase}
.f-links{left:371px;top:2479px;list-style:none;font:400 12.5px/25.6px "Raleway",sans-serif;color:#fff}
.f-contact{font:400 13px/20px "Raleway",sans-serif;color:#fff}
.field{border:1px solid #ddd;border-radius:3px;color:#fff;font:400 11px "Raleway",sans-serif;padding:10px 12px}
.send{left:831px;top:2606px;width:117px;height:36px;background:var(--navy);color:#fff;font:500 11px/36px "Roboto",sans-serif;text-align:center;text-transform:uppercase}

.bottombar{left:0;top:2685px;width:1200px;height:55px;background:var(--navy)}
.copy{left:99px;top:2705px;font:400 13px "Raleway",sans-serif;color:#fff}
.b-social{left:950px;top:2695px;display:flex;gap:10px}
.b-social span{width:34px;height:34px;border-radius:50%;border:2px solid #fff}
</style>
</head>
<body>
<div class="page">

  <!-- top bar -->
  <div class="abs topbar"></div>
  <div class="abs topbar phone">
    <svg width="22" height="22" viewBox="0 0 22 22"><circle cx="11" cy="11" r="10" fill="none" stroke="#fff" stroke-width="1.5"/><path d="M7.5 6.5c.6-.6 1.4-.5 1.8.1l.8 1.3c.3.5.2 1.1-.2 1.4l-.6.5c.5 1.2 1.4 2.1 2.6 2.6l.5-.6c.4-.4 1-.5 1.4-.2l1.3.8c.6.4.7 1.2.1 1.8-1 1-2.6 1.1-4.4-.1-1.5-1-2.5-2.1-3.3-3.6-.9-1.6-.8-3 0-4z" fill="#fff"/></svg>
    1800 4417 2290
  </div>
  <div class="abs topbar divider"></div>
  <div class="abs topbar social"><span></span><span></span><span></span><span></span><span></span></div>

  <!-- header -->
  <div class="abs header"></div>
  <div class="abs brand"><div class="mark"></div><div class="name">Harlow Mechanical Contractors</div></div>
  <nav class="abs nav">
    <a class="active" style="left:0">Home</a>
    <a style="left:71px">About Us</a>
    <a style="left:166px">Plumbing Services</a>
    <a style="left:327px">Blog Posts</a>
    <a style="left:431px">Contact Us</a>
  </nav>

  <!-- hero -->
  <div class="abs hero" role="img" aria-label="Photo of a plumber tightening a pipe fitting with a wrench"></div>
  <h1 class="abs hero-title">Harlow Mechanical Contractors</h1>
  <p class="abs hero-sub">We install full plumbing services for large offices, condominiums,<br>and industrial projects.</p>
  <svg class="abs hero-arrow" style="left:30px" width="24" height="44" viewBox="0 0 24 44"><path d="M20 2 L4 22 L20 42" fill="none" stroke="#fff" stroke-width="2"/></svg>
  <svg class="abs hero-arrow" style="left:1146px" width="24" height="44" viewBox="0 0 24 44"><path d="M4 2 L20 22 L4 42" fill="none" stroke="#fff" stroke-width="2"/></svg>

  <!-- service circles -->
  <div class="abs circle" style="left:122px;background:linear-gradient(135deg,#f2f2f2,#d8c9b0 50%,#c9a36a)" role="img" aria-label="Photo of brass pipe fittings and a hard hat on blueprints"></div>
  <div class="abs circle mid" style="left:482px;background:linear-gradient(135deg,#e9ecef,#9aa3ab 50%,#5a636b)" role="img" aria-label="Photo of a chrome faucet"></div>
  <div class="abs circle" style="left:829px;background:linear-gradient(135deg,#dfe6ee,#6d8fb8 50%,#2f5a9e)" role="img" aria-label="Photo of a contractor at a desk on the phone"></div>

  <h2 class="abs svc-title" style="left:96px">Large Offices</h2>
  <p class="abs svc-text" style="left:111px">Quisque ligulas ipsum, euismod atras vulpu tate iltricies etri elit. Class aptent taciti soci osqu ad litora torquent per conubia</p>
  <div class="abs svc-more" style="left:96px">READ MORE <svg width="14" height="14" viewBox="0 0 14 14"><circle cx="7" cy="7" r="7" fill="var(--brand)"/><path d="M5.5 4 L8.5 7 L5.5 10" fill="none" stroke="#fff" stroke-width="1.8"/></svg></div>

  <h2 class="abs svc-title" style="left:456px">Condominiums</h2>
  <p class="abs svc-text" style="left:471px">Quisque ligulas ipsum, euismod atras vulpu tate iltricies etri elit. Class aptent taciti soci osqu ad litora torquent per conubia</p>
  <div class="abs svc-more" style="left:456px">READ MORE <svg width="14" height="14" viewBox="0 0 14 14"><circle cx="7" cy="7" r="7" fill="var(--brand)"/><path d="M5.5 4 L8.5 7 L5.5 10" fill="none" stroke="#fff" stroke-width="1.8"/></svg></div>

  <h2 class="abs svc-title" style="left:803px">Industrial Projects</h2>
  <p class="abs svc-text" style="left:818px">Quisque ligulas ipsum, euismod atras vulpu tate iltricies etri elit. Class aptent taciti soci osqu ad litora torquent per conubia</p>
  <div class="abs svc-more" style="left:803px">READ MORE <svg width="14" height="14" viewBox="0 0 14 14"><circle cx="7" cy="7" r="7" fill="var(--brand)"/><path d="M5.5 4 L8.5 7 L5.5 10" fill="none" stroke="#fff" stroke-width="1.8"/></svg></div>

  <div class="abs rule" style="left:99px;top:958px;width:1002px"></div>

  <!-- about -->
  <h2 class="abs sec-title" style="left:333px;top:1004px"><span class="dot"></span>Harlow Mechanical Contractors</h2>
  <p class="abs intro">Kitaesaert tasetruse aplicaserde neafaese mikertyu eraneo. Nsatolernatur aut oditaut Beasnseq usauntur magni dolores eo qui ratione voluptate msequi nesciuque porro quisqu ameras dolomasereta jrease kuytras masertqui dolorem ipsum, quiadesa dolores. Kitaesaert tasetruse aplicaserde neafaese mikertyu eraneo. Nsatolernatur aut oditaut Beasnseq usauntur magni dolores eo qui ratione voluptate msequi nesciuque porro quisqu ameras doloma sereta jrease kuytras masertqui dolorem ipsum, quiadesa dolores.</p>

  <div class="abs tile" style="left:99px;background:var(--tile-a)">
    <svg width="80" height="80" viewBox="0 0 80 80"><rect x="6" y="18" width="68" height="16" rx="4" fill="none" stroke="#fff" stroke-width="4"/><rect x="2" y="14" width="10" height="24" rx="2" fill="#fff"/><rect x="68" y="14" width="10" height="24" rx="2" fill="#fff"/><path d="M40 42 C35 52 34 56 40 58 C46 56 45 52 40 42z" fill="#fff"/></svg>
    <div class="label">Leak Detection</div>
  </div>
  <div class="abs tile" style="left:354px;background:var(--tile-b)">
    <svg width="80" height="80" viewBox="0 0 80 80"><rect x="34" y="6" width="12" height="6" fill="#fff"/><rect x="22" y="12" width="36" height="6" rx="3" fill="#fff"/><rect x="32" y="18" width="16" height="12" fill="#fff"/><path d="M14 30 H56 V44 H44 V38 H14z" fill="#fff"/><path d="M50 52 C46 60 45 64 50 66 C55 64 54 60 50 52z" fill="#fff"/></svg>
    <div class="label">Water Line Repair</div>
  </div>
  <div class="abs tile" style="left:610px;background:var(--tile-c)">
    <svg width="80" height="80" viewBox="0 0 80 80"><circle cx="44" cy="10" r="3" fill="#fff"/><circle cx="52" cy="14" r="3" fill="#fff"/><circle cx="44" cy="20" r="3" fill="#fff"/><circle cx="54" cy="24" r="3" fill="#fff"/><path d="M4 34 H76" stroke="#fff" stroke-width="5"/><path d="M10 36 V46 C10 56 18 60 26 60 H54 C62 60 70 56 70 46 V36" fill="none" stroke="#fff" stroke-width="5"/><path d="M22 60 L18 68 M58 60 L62 68" stroke="#fff" stroke-width="5"/></svg>
    <div class="label">Bathroom Plumbing</div>
  </div>
  <div class="abs tile" style="left:865px;background:var(--tile-d)">
    <svg width="80" height="80" viewBox="0 0 80 80"><rect x="20" y="4" width="20" height="8" fill="#fff"/><rect x="24" y="12" width="12" height="24" fill="#fff"/><path d="M24 36 H52 V44 H24z" fill="#fff"/><rect x="44" y="44" width="12" height="12" fill="#fff"/><rect x="40" y="56" width="20" height="6" fill="#fff"/><path d="M50 64 C46 72 46 74 50 76 C54 74 54 72 50 64z" fill="#fff"/></svg>
    <div class="label">Plumbing Repair</div>
  </div>

  <!-- blue band -->
  <div class="abs band" role="img" aria-label="Faded photo of plumbers at work under a blue overlay"></div>
  <h2 class="abs band-title" style="left:99px;top:1482px"><span class="dot"></span>Commercial Plumbing Services</h2>
  <h2 class="abs band-title" style="left:716px;top:1482px"><span class="dot"></span>Popular Services</h2>

  <div class="abs card" style="left:99px">
    <div class="photo" style="background:linear-gradient(135deg,#4d6fa8,#c9d13b 60%,#3a3a3a)" role="img" aria-label="Photo of a plumber in a hi-vis vest working on pipes"></div>
    <h3>Plumbing Services</h3>
    <p>Nemo enim ipsam voluptatem quia voluptas sit aspernatur aut odit aut fugit, sed quia conse quuntur magni dolores eosqui</p>
    <div class="btn" style="background:var(--brand)">Read More</div>
  </div>
  <div class="abs card" style="left:393px">
    <div class="photo" style="background:linear-gradient(135deg,#6b4a38,#c9b7a6 50%,#8c3b2f)" role="img" aria-label="Photo of a worker cutting white pipe"></div>
    <h3>Commercial Services</h3>
    <p>Nemo enim ipsam voluptatem quia voluptas sit aspernatur aut odit aut fugit, sed quia conse quuntur magni dolores eosqui</p>
    <div class="btn" style="background:#6a6a6a">Read More</div>
  </div>

  <div class="abs pop-thumb" style="top:1569px;background:linear-gradient(135deg,#8a8f94,#d8dadc)" role="img" aria-label="Photo of pipework under a sink"></div>
  <div class="abs pop-title" style="top:1572px">Industrial Projects</div>
  <p class="abs pop-text" style="top:1606px">Soera wisi et urna. Aliquam eratoltpas kasya saceratunteger rutrum kertyua.</p>
  <div class="abs pop-rule" style="top:1667px"></div>

  <div class="abs pop-thumb" style="top:1684px;background:linear-gradient(135deg,#7a6e66,#c8c2bc)" role="img" aria-label="Photo of a plumber fitting a pipe"></div>
  <div class="abs pop-title" style="top:1687px">Condominium Projects</div>
  <p class="abs pop-text" style="top:1721px">Soera wisi et urna. Aliquam eratoltpas kasya saceratunteger rutrum kertyua.</p>
  <div class="abs pop-rule" style="top:1782px"></div>

  <div class="abs pop-thumb" style="top:1799px;background:linear-gradient(135deg,#6d747b,#b9bec3)" role="img" aria-label="Photo of a wrench on a pipe joint"></div>
  <div class="abs pop-title" style="top:1802px">Large office Projects</div>
  <p class="abs pop-text" style="top:1836px">Soera wisi et urna. Aliquam eratoltpas kasya saceratunteger rutrum kertyua.</p>

  <!-- why call us -->
  <h2 class="abs sec-title" style="left:486px;top:1980px"><span class="dot"></span>Why Call Us</h2>

  <svg class="abs feature-icon" style="left:99px" width="44" height="44" viewBox="0 0 44 44"><circle cx="22" cy="13" r="9" fill="var(--brand)"/><path d="M4 44 C4 30 12 25 22 25 C32 25 40 30 40 44z" fill="var(--brand)"/></svg>
  <h3 class="abs feature-title" style="left:164px">Superior Technicians</h3>
  <p class="abs feature-text" style="left:164px">All our technicians are thoroughly vetted, trained, licensed, experienced, and bonded, long before they enter</p>

  <svg class="abs feature-icon" style="left:444px" width="44" height="44" viewBox="0 0 44 44"><rect x="3" y="7" width="38" height="35" fill="none" stroke="var(--brand)" stroke-width="3"/><rect x="3" y="7" width="38" height="8" fill="var(--brand)"/><rect x="11" y="2" width="4" height="9" fill="var(--brand)"/><rect x="29" y="2" width="4" height="9" fill="var(--brand)"/><g fill="var(--brand)"><rect x="9" y="20" width="6" height="5"/><rect x="19" y="20" width="6" height="5"/><rect x="29" y="20" width="6" height="5"/><rect x="9" y="30" width="6" height="5"/><rect x="19" y="30" width="6" height="5"/><rect x="29" y="30" width="6" height="5"/></g></svg>
  <h3 class="abs feature-title" style="left:504px">Same Day Service</h3>
  <p class="abs feature-text" style="left:504px">All our technicians are thoroughly vetted, trained, licensed, experienced, and bonded, long before they enter</p>

  <svg class="abs feature-icon" style="left:791px" width="44" height="44" viewBox="0 0 44 44"><rect x="3" y="18" width="9" height="22" fill="none" stroke="var(--brand)" stroke-width="3"/><path d="M14 20 L22 4 C26 4 27 8 26 12 L25 17 H38 C41 17 42 20 41 23 L37 38 C36 40 35 41 32 41 H14z" fill="none" stroke="var(--brand)" stroke-width="3"/></svg>
  <h3 class="abs feature-title" style="left:849px">100% Satisfaction Guarantee</h3>
  <p class="abs feature-text" style="left:849px">All our technicians are thoroughly vetted, trained, licensed, experienced, and bonded, long before they enter</p>

  <div class="abs rule" style="left:99px;top:2211px;width:1002px;height:1px"></div>

  <!-- partners -->
  <svg class="abs" style="left:79px;top:2275px" width="36" height="36" viewBox="0 0 36 36"><circle cx="18" cy="18" r="16" fill="none" stroke="#333" stroke-width="2"/><path d="M20 11 L13 18 L20 25" fill="none" stroke="#333" stroke-width="2.5"/></svg>
  <svg class="abs" style="left:1083px;top:2275px" width="36" height="36" viewBox="0 0 36 36"><circle cx="18" cy="18" r="16" fill="none" stroke="#333" stroke-width="2"/><path d="M16 11 L23 18 L16 25" fill="none" stroke="#333" stroke-width="2.5"/></svg>
  <div class="abs partners">
    <div class="partner"><svg width="60" height="40"><rect x="0" y="8" width="60" height="24" rx="4" fill="#444"/></svg></div>
    <div class="partner-sep"></div>
    <div class="partner"><svg width="60" height="40"><rect x="0" y="8" width="60" height="24" rx="4" fill="#444"/></svg></div>
    <div class="partner-sep"></div>
    <div class="partner"><svg width="60" height="50"><circle cx="30" cy="25" r="22" fill="#444"/></svg></div>
    <div class="partner-sep"></div>
    <div class="partner"><svg width="60" height="50"><circle cx="30" cy="25" r="22" fill="#555"/></svg></div>
    <div class="partner-sep"></div>
    <div class="partner"><svg width="60" height="50"><rect x="4" y="6" width="52" height="38" rx="3" fill="#444"/></svg></div>
    <div class="partner-sep"></div>
    <div class="partner"><svg width="60" height="50"><circle cx="30" cy="25" r="22" fill="#444"/></svg></div>
  </div>

  <!-- footer -->
  <div class="abs footer" role="img" aria-label="Faded dark photo of pipework behind the footer"></div>
  <div class="abs f-brand"><div class="mark"></div><div class="name">Harlow Mechanical Contractors</div></div>

  <div class="abs f-head" style="left:371px">Quick Link</div>
  <ul class="abs f-links">
    <li>&gt;&nbsp; Home</li><li>&gt;&nbsp; Services</li><li>&gt;&nbsp; About Us</li><li>&gt;&nbsp; Blog Post</li><li>&gt;&nbsp; Why Choose Us</li><li>&gt;&nbsp; Contact Us</li>
  </ul>

  <div class="abs f-head" style="left:557px">Contact Us</div>
  <svg class="abs" style="left:557px;top:2484px" width="12" height="16" viewBox="0 0 12 16"><path d="M6 0 C2.7 0 0 2.6 0 5.8 C0 10 6 16 6 16 C6 16 12 10 12 5.8 C12 2.6 9.3 0 6 0z" fill="#fff"/><circle cx="6" cy="6" r="2.2" fill="#2b2b2b"/></svg>
  <p class="abs f-contact" style="left:584px;top:2479px">Harlow Mechanical Contractors,<br>3rd Floor, 48 Kestrel Lane,<br>Northbridge.</p>
  <svg class="abs" style="left:557px;top:2560px" width="14" height="14" viewBox="0 0 14 14"><path d="M2 1 C3 0 4 0 4.6 1 L5.8 3 C6.2 3.7 6 4.4 5.5 4.8 L4.7 5.4 C5.4 7 6.8 8.4 8.5 9.2 L9.1 8.4 C9.6 7.9 10.3 7.8 11 8.2 L13 9.4 C14 10 14 11 13 12 C11.4 13.6 9 13.6 6 11.4 C4 9.9 2.8 8.6 1.6 6.6 C.2 4.2 .5 2.5 2 1z" fill="#fff"/></svg>
  <p class="abs f-contact" style="left:584px;top:2557px">Help:&nbsp;&nbsp; + 1-555-310-4782</p>
  <svg class="abs" style="left:557px;top:2599px" width="14" height="11" viewBox="0 0 14 11"><rect width="14" height="11" fill="#fff"/><path d="M0 0 L7 6 L14 0" fill="none" stroke="#2b2b2b" stroke-width="1.4"/></svg>
  <p class="abs f-contact" style="left:584px;top:2595px">Mail:&nbsp;&nbsp; info@harlowmc.example</p>

  <div class="abs f-head" style="left:831px">Contact Form</div>
  <div class="abs field" style="left:831px;top:2480px;width:128px;height:38px">Name</div>
  <div class="abs field" style="left:970px;top:2480px;width:129px;height:38px">Phone</div>
  <div class="abs field" style="left:831px;top:2524px;width:268px;height:65px">Message</div>
  <div class="abs send">Send Message</div>

  <div class="abs bottombar"></div>
  <p class="abs copy">© 2016 Harlow Mechanical Contractors. All Rights Reserved.</p>
  <div class="abs b-social"><span></span><span></span><span></span><span></span></div>

</div>
</body>
</html>
```